letterhead design using our existing logo

We are a small boutique property management business based in Sydney's Northern Beaches.
We are after a sleek, simple modern letterhead (A4) incorporating our logo and its colours.
Also matching envelope (DL)
I have attached the logo with black text and white text for design options.

Target Market(s)

29-69yo Male and Female

Industry/Entity Type

Property Management

Requirements
Must have
• - Estate Haven logo
• - Address, number and website:
• Suite 7, 18-19 Harlow Parade, Brenton NSW 2187
• Tel: Carl Doyle 0419 267 530 Miriam Kovacs 0407 516 948 www.estatehavenrealty.com.au
Nice to have
• sleek design that looks modern and professional
Should not have
• too many colours or too busy

```html
<!DOCTYPE html>
<html lang="en">
<head>
<meta charset="utf-8">
<title>Estate Haven — Letterhead &amp; Envelope</title>
<link href="https://fonts.googleapis.com/css2?family=Didact+Gothic&family=Lato:wght@400;700;900&display=swap" rel="stylesheet">
<style>
  :root {
    --backdrop: #e4e8ea;
    --paper: #ffffff;
    --envelope: #efefef;
    --teal: #3a9593;
    --ink: #111111;
    --body: #3c3c3c;
    --watermark: rgba(120, 120, 120, 0.28);
  }
  * { margin: 0; padding: 0; box-sizing: border-box; }
  html, body { width: 1200px; height: 784px; overflow: hidden; }
  body {
    background: radial-gradient(ellipse at 50% 40%, #f2f4f5 0%, var(--backdrop) 100%);
    position: relative;
    font-family: "Didact Gothic", "Century Gothic", sans-serif;
  }
  .sheet {
    position: absolute;
    top: 45px;
    width: 513px;
    height: 697px;
    border-radius: 12px;
    overflow: hidden;
    box-shadow: 0 2px 6px rgba(0,0,0,0.18);
  }
  .letterhead { left: 42px; background: var(--paper); }
  .envelope { left: 634px; background: var(--envelope); }

  .brand {
    position: absolute;
    font-family: "Lato", sans-serif;
    font-weight: 900;
    color: var(--ink);
    white-space: nowrap;
    letter-spacing: -0.3px;
  }
  .letterhead .brand { top: 55px; left: 0; width: 100%; text-align: center; font-size: 22px; }
  .envelope .brand { top: 566px; left: 112px; font-size: 34px; }

  .letter-body {
    position: absolute;
    top: 148px;
    left: 50px;
    width: 421px;
    font-size: 10.4px;
    line-height: 17.4px;
    color: var(--body);
    text-align: justify;
  }
  .letter-body p + p { margin-top: 18px; }

  .watermark {
    position: absolute;
    top: 334px;
    left: 0;
    width: 100%;
    text-align: center;
    font-family: "Lato", sans-serif;
    font-weight: 900;
    font-size: 30px;
    color: var(--watermark);
    pointer-events: none;
  }

  .signature { position: absolute; top: 583px; left: 383px; }
  .signature .name { font-size: 14px; color: #222; }
  .signature .role { font-size: 9.5px; color: #333; margin-top: 6px; }

  .website {
    position: absolute;
    top: 645px;
    width: 100%;
    text-align: center;
    font-family: "Lato", sans-serif;
    font-weight: 700;
    font-size: 10.5px;
    letter-spacing: 2.4px;
    color: var(--teal);
  }
  .contact-band {
    position: absolute;
    bottom: 0;
    left: 0;
    width: 100%;
    height: 32px;
    background: var(--teal);
    display: flex;
    align-items: center;
    justify-content: center;
    gap: 22px;
    font-family: "Lato", sans-serif;
    font-weight: 700;
    font-size: 7.8px;
    color: #ffffff;
  }
</style>
</head>
<body>

<section class="sheet letterhead">
  <div class="brand">ESTATE HAVEN</div>

  <div class="watermark" aria-hidden="true">ESTATE HAVEN</div>

  <div class="letter-body">
    <p>Lorem ipsum dolor sit amet, consectetur adipiscing elit. Donec orci purus, luctus vitae dignissim eu, iaculis sed purus. Vivamus faucibus, ipsum nec aliquet viverra, leo mauris condimentum ligula, sit amet sagittis enim ligula quis arcu. Nam egestas tortor id nisi porttitor mattis. In tortor ante, ultricies in suscipit a, tempus non massa. Vivamus et auctor mi. Fusce vel massa nulla. Phasellus nec eros mauris, et scelerisque orci. Donec malesuada orci vitae nulla accumsan porta a id massa.</p>
    <p>Quisque accumsan iaculis magna sit amet fringilla. Maecenas consequat, magna eget tincidunt semper, odio nibh rutrum mi, id feugiat ante nisi eu risus. Vestibulum nunc orci, rhoncus a placerat in, ultricies in mi. Cras mattis varius eros, vel fringilla nisi suscipit eget. Quisque scelerisque sagittis nulla at porttitor. Mauris a justo et tellus interdum tristique. Sed id augue vitae urna euismod commodo aliquet a quam. Pellentesque arcu velit, cursus et malesuada ut, consequat et diam. Nullam erat sem, rhoncus id ullamcorper vitae, rhoncus et arcu. In ultricies ultricies nulla.</p>
    <p>Kut rutrum nisi iaculis at. Donec eu magna a metus ornare faucibus. Fusce aliquet faucibus ultricies. Morbi semper, est id tincidunt gravida, sem arcu adipiscing lacus, ac bibendum nulla leo eu purus. Quisque nec diam sed risus consectetur a ccumsan quis quis nibh. Vestibulum id purus lorem. Donec eu magna a metus ornare faucibus. Fusce aliquet faucibus ultricies. Morbi semper, est id tincidunt gravida, sem arcu adipiscing lacus, ac bibendum nulla leo eu purus. Quisque nec diam sed risus consectetur a ccumsan quis quis nibh. Vestibulum id purus lorem.</p>
  </div>

  <div class="signature">
    <div class="name">Owen Hartley</div>
    <div class="role">Co-Founder &amp; CEO</div>
  </div>

  <div class="website">www.estatehavenrealty.com.au</div>

  <footer class="contact-band">
    <span>Carl Doyle: 0419 267 530</span>
    <span>Miriam Kovacs: 0407 516 948</span>
    <span>Suite 7, 18-19 Harlow Parade, Brenton NSW 2187</span>
  </footer>
</section>

<section class="sheet envelope">
  <div class="brand">ESTATE HAVEN</div>
</section>

</body>
</html>
```